Tessellaria

Club flyer, grand opening night, house/electronic music, looking for clean design with a sample image attached. Please look at the prior flyers to get an idea of the style. Guaranteed project
I would like to use the red design if possible (tessellaria flyer attached)
Text:
TESSELLARIA
Winter House Music Monthly
Opening Night Dec 13 2013
Pellmont (use logo)
Featuring
BRAMOX (House/Garage)
(use logo with just Bramox name)
w/ resident
ORV (Driftwerk)
Free All Night
21-39 year old club with all house/electronic music. classier and grown up over gimmicky
Club

```html
<!DOCTYPE html>
<html lang="en">
<head>
<meta charset="utf-8">
<title>Tessellaria – Opening Night Flyer</title>
<link rel="stylesheet" href="https://fonts.googleapis.com/css2?family=Source+Sans+3:wght@300;400;700&family=PT+Sans+Narrow:wght@700&display=swap">
<style>
  :root {
    --board-top: #5a5a5a;
    --board-bottom: #111111;
    --band: #6b6b6b;
    --paper: #ffffff;
    --navy: #24408e;
    --rose: #e62a76;
    --rose-tab: #d6457f;
    --rose-deep: #ee2c6c;
    --rose-mid: #f3628f;
    --rose-soft: #f8b6ca;
    --rose-pale: #fbe0e8;
  }
  * { box-sizing: border-box; margin: 0; padding: 0; }
  html, body { width: 1200px; height: 900px; overflow: hidden; }
  body {
    position: relative;
    background: linear-gradient(135deg, var(--board-top) 0%, #3a3a3a 55%, var(--board-bottom) 100%);
    font-family: "Source Sans 3", "Myriad Pro", sans-serif;
  }
  .board-band {
    position: absolute; left: 0; top: 790px; width: 1200px; height: 110px;
    background: var(--band);
  }
  .flyer {
    position: absolute; top: 47px; width: 495px; height: 700px;
    background: var(--paper);
    overflow: hidden;
    box-shadow: 4px 5px 10px rgba(0,0,0,0.55);
    --accent: var(--navy);
    --tab: var(--navy);
  }
  .flyer--navy { left: 85px; }
  .flyer--rose { left: 634px; --accent: var(--rose); --tab: var(--rose-tab); }

  .burst {
    position: absolute; left: -340px; top: 60px; width: 680px; height: 680px;
    border-radius: 50%;
    background: radial-gradient(circle at center,
      var(--rose-pale) 0%, var(--rose-soft) 6%, var(--rose-deep) 16%,
      var(--rose-deep) 30%, var(--rose-mid) 46%, var(--rose-soft) 64%,
      rgba(251,224,232,0.5) 80%, rgba(255,255,255,0) 100%);
  }

  .tab {
    position: absolute; left: 0; top: 0; width: 43px; height: 150px;
    background: var(--tab);
    display: flex; align-items: center; justify-content: center;
  }
  .tab-text {
    transform: rotate(90deg);
    white-space: nowrap;
    color: #fff; font-weight: 700; font-size: 15px; letter-spacing: 0.3px;
  }
  .headliner {
    position: absolute; right: 42px; top: 44px;
    color: var(--accent);
    font-weight: 700; font-size: 28px; letter-spacing: 1px;
  }
  .title {
    position: absolute; left: 0; top: 124px; width: 495px; padding-left: 4px;
    text-align: center;
    color: var(--rose);
    font-weight: 300; font-size: 48px; letter-spacing: 0.5px; line-height: 1;
  }
  .subtitle {
    position: absolute; left: 0; top: 173px; width: 495px; padding-left: 4px;
    text-align: center;
    color: var(--rose);
    font-family: "PT Sans Narrow", "Myriad Pro Condensed", sans-serif;
    font-weight: 700; font-size: 17px; letter-spacing: 0.3px;
  }
  .date-box {
    position: absolute; left: 114px; top: 374px; width: 282px; height: 33px;
    background: var(--paper);
    border: 1px solid var(--rose);
    display: flex; align-items: center; justify-content: center;
    color: var(--accent);
    font-family: "PT Sans Narrow", "Myriad Pro Condensed", sans-serif;
    font-weight: 700; font-size: 20px; letter-spacing: 0.2px;
  }
  .venue {
    position: absolute; left: 0; top: 604px; width: 520px;
    text-align: center;
    color: var(--rose);
    font-size: 17px; font-weight: 400; letter-spacing: 1px;
  }
  .resident {
    position: absolute; left: 0; top: 646px; width: 520px;
    text-align: center;
    color: var(--rose);
    font-size: 24px; font-weight: 400; letter-spacing: 4px;
  }
</style>
</head>
<body>
  <div class="board-band"></div>

  <article class="flyer flyer--navy">
    <div class="burst" role="img" aria-label="Pink kaleidoscopic burst illustration radiating from the left edge"></div>
    <div class="tab"><span class="tab-text">Free All Night</span></div>
    <div class="headliner">BRAMOX</div>
    <h1 class="title">TESSELLARIA</h1>
    <p class="subtitle">WINTER HOUSE MUSIC MONTHLY</p>
    <p class="date-box">OPENING NIGHT DEC 13 2013</p>
    <p class="venue">PELLMONT</p>
    <p class="resident">DRIFTWERK</p>
  </article>

  <article class="flyer flyer--rose">
    <div class="burst" role="img" aria-label="Pink kaleidoscopic burst illustration radiating from the left edge"></div>
    <div class="tab"><span class="tab-text">Free All Night</span></div>
    <div class="headliner">BRAMOX</div>
    <h1 class="title">TESSELLARIA</h1>
    <p class="subtitle">WINTER HOUSE MUSIC MONTHLY</p>
    <p class="date-box">OPENING NIGHT DEC 13 2013</p>
    <p class="venue">PELLMONT</p>
    <p class="resident">DRIFTWERK</p>
  </article>
</body>
</html>
```